Maple Yard Works Website Design

I need a 6 page website design for a company that Installs Synthetic Turf, Interlocking Pavers, and Patio Covers. We would like to see the design us "Landscaping Style" of a look and feel. Green, Blacks and Gray colors. Initially the website will be used the online brochure but landing pages will need to be built form this original design. Since this is brand new start up (actually offshoot form another company I was part of) we are limited on photography. We will need to use stock images until i can get installed projects photographed.This is a B2C site...targeting homeowners who are looking to expand their back yards or simply transition to maintenance free and drought tolerant yards. This is becoming very popular in California and along the Southwest United States.

Target Market(s)

Homeowners

Industry/Entity Type

Home Improvement

Coding

Coded - Design and coding required

Number of Pages Required

1 page

Font styles to use
Sans Serif

Colors
9bcb3b

Requirements
Must have
• Strong visuals and some graphic elements to illustrate the services.
• Here are some sample sites:
• https://brelvanstone.com
• https://www.quintaleaf.net/
• https://plomaris.com/BackyardHomePage
• https://otterlawns.com
• https://www.greskano.com/
• http://www.brookvalestones.com/
• https://meadowblendsupplyco.com/
• https://decktraderdepotco.com
• https://www.welbrickbuilders.com

```html
<!DOCTYPE html>
<html lang="en">
<head>
<meta charset="utf-8">
<title>Maple Yard Works</title>
<link rel="stylesheet" href="https://fonts.googleapis.com/css2?family=Poppins:wght@300;400;500;600;700&family=Open+Sans:wght@400;600&display=swap">
<style>
:root{
  --green:#9bcb3b;
  --green-dark:#86b52c;
  --ink:#222;
  --text:#555;
  --muted:#777;
  --dark:#444;
  --black:#111;
  --footer:#222;
  --gray-bg:#e9e9e9;
  --light-bg:#f4f4f4;
  --white:#fff;
}
*{box-sizing:border-box;margin:0;padding:0}
html,body{width:1200px;height:4532px;overflow:hidden}
body{font-family:"Open Sans",sans-serif;color:var(--text);background:var(--white);position:relative}
.abs{position:absolute}
.heading{font-family:"Poppins",sans-serif;font-weight:700;color:var(--green);text-transform:uppercase;letter-spacing:-0.5px}
.center{text-align:center;left:0;width:1200px}
.btn{position:absolute;display:flex;align-items:center;justify-content:center;gap:22px;font-family:"Poppins",sans-serif;font-weight:500;font-size:20px;color:var(--white);background:var(--dark);clip-path:polygon(14px 0,100% 0,calc(100% - 14px) 100%,0 100%)}
.btn svg{width:10px;height:14px}

/* top bar */
.topbar{top:0;left:0;width:1200px;height:28px;background:var(--black);color:var(--white);font-size:13px}
.topbar span{position:absolute;left:88px;top:5px}

/* header */
.header{top:28px;left:0;width:1200px;height:90px;background:var(--white)}
.brand{left:98px;top:22px;display:flex;align-items:center;gap:18px}
.brand-mark{width:44px;height:44px;border-radius:50%;background:var(--green)}
.brand-name{font-family:"Poppins",sans-serif;font-weight:600;font-size:21px;line-height:24px;color:var(--ink);width:170px}
.info{display:flex;align-items:center;gap:14px;top:20px}
.info svg{width:42px;height:42px}
.info b{display:block;font-family:"Poppins",sans-serif;font-weight:600;font-size:21px;color:var(--ink);line-height:26px}
.info small{font-size:14px;color:var(--text)}

/* nav */
.nav{top:118px;left:0;width:1200px;height:54px;background:var(--green);display:flex;justify-content:center;gap:38px;padding-left:10px}
.nav a{font-family:"Poppins",sans-serif;font-size:17px;color:var(--white);text-decoration:none;line-height:54px}
.nav a::after{content:"";display:inline-block;margin-left:4px;border:4px solid transparent;border-top-color:var(--white);transform:translateY(3px)}

/* hero */
.hero{top:172px;left:0;width:1200px;height:583px;background:linear-gradient(180deg,#3d4a33 0%,#6b4d3c 35%,#7a5b44 55%,#5d8a35 75%,#4f7a2c 100%)}
.hero::after{content:"";position:absolute;inset:0;background:linear-gradient(90deg,rgba(0,0,0,.35),rgba(0,0,0,.05))}
.hero-title{left:88px;top:118px;z-index:1;font-family:"Poppins",sans-serif;font-weight:700;font-size:54px;color:var(--white);text-transform:uppercase;letter-spacing:-1px}
.hero-text{left:88px;top:200px;z-index:1;font-size:19px;line-height:32px;color:var(--white)}
.hero .btn{left:90px;top:294px;width:322px;height:74px;z-index:1;background:var(--white);color:var(--ink);clip-path:polygon(24px 0,100% 0,calc(100% - 24px) 100%,0 100%)}
.dots{top:525px;left:556px;z-index:1;display:flex;gap:16px}
.dots i{width:17px;height:17px;border-radius:50%;border:2px solid var(--white);display:block}
.dots i.on{background:radial-gradient(var(--white) 3px,transparent 4px)}

/* about */
.about{top:755px;left:0;width:1200px;height:505px;background:var(--white)}
.about .heading{left:93px;top:78px;font-size:40px}
.about p{left:93px;top:152px;width:497px;font-size:14.5px;line-height:31px;text-align:justify}
.about .btn{left:90px;top:332px;width:242px;height:63px}
.about-photo{left:654px;top:79px;width:454px;height:325px;border:7px solid var(--white);box-shadow:0 2px 14px rgba(0,0,0,.3);background:linear-gradient(135deg,#b9a99a 0%,#c9b7a5 35%,#6f9a3a 60%,#4d7a2a 100%)}

/* services */
.services{top:1260px;left:0;width:1200px;height:733px;background:var(--gray-bg)}
.services .heading,.gallery .heading{font-size:40px;top:46px}
.lead{font-size:16.5px;line-height:28px;color:var(--ink)}
.services .lead{top:120px}
.service{width:276px;text-align:center}
.service .ring{width:262px;height:262px;border-radius:50%;border:6px solid var(--green);margin:0 auto}
.service h3{font-family:"Poppins",sans-serif;font-weight:600;color:var(--green);font-size:21px;margin-top:44px;text-transform:uppercase}
.service p{margin-top:20px;font-size:15px;line-height:27px;text-align:justify;text-align-last:center;color:var(--muted)}

/* gallery */
.gallery{top:1993px;left:0;width:1200px;height:962px;background:var(--white)}
.gallery .lead{top:164px}
.tile{position:absolute}
.gallery .btn{left:485px;top:820px;width:275px;height:63px}

/* testimonials */
.testimonials{top:2955px;left:0;width:1200px;height:677px;background:var(--light-bg)}
.quote-box{left:561px;top:50px;width:99px;height:80px;background:var(--white);border:1px solid #ddd;display:flex;align-items:center;justify-content:center}
.testimonials .heading{top:160px;font-size:40px}
.card{top:268px;width:440px;height:221px;background:var(--white);border:1px solid #ddd;padding:19px 16px}
.card .avatar{position:absolute;left:14px;top:19px;width:63px;height:51px;background:linear-gradient(180deg,#8a7d6b,#5b4d40)}
.card .who{position:absolute;left:98px;top:20px}
.card .who b{display:block;font-family:"Poppins",sans-serif;font-weight:600;font-size:21px;color:var(--green);text-transform:uppercase;line-height:26px}
.card .who small{font-size:14px;color:var(--text)}
.card .qmark{position:absolute;right:42px;top:24px}
.card p{position:absolute;left:16px;top:95px;width:400px;font-size:15px;line-height:27px}
.card p a{color:var(--green);font-weight:600;text-decoration:none}
.testimonials .btn{left:456px;top:556px;width:311px;height:62px}

/* contact */
.contact{top:3632px;left:0;width:1200px;height:484px;background:var(--white)}
.footer{top:4116px;left:0;width:1200px;height:416px;background:var(--footer)}
.contact-card{top:3712px;left:123px;width:952px;height:571px;background:var(--white);border:1px solid #ddd;box-shadow:0 0 6px rgba(0,0,0,.05)}
.contact-card .heading{font-size:40px;top:36px;left:0;width:950px;text-align:center}
.touch{left:58px;top:140px;width:289px;height:373px;background:var(--green);color:var(--white)}
.touch h4{font-family:"Poppins",sans-serif;font-weight:600;font-size:21px;text-align:center;margin-top:68px;text-transform:uppercase}
.touch .row{position:absolute;left:0;width:289px;display:flex;gap:24px;padding-left:28px;font-size:15px;line-height:22px;border-top:1px solid rgba(255,255,255,.35)}
.touch svg{width:16px;height:18px;flex:none;margin-top:2px}
.talk{left:382px;top:172px;font-family:"Poppins",sans-serif;font-weight:600;font-size:19px;color:var(--ink)}
.field{left:382px;width:454px;border-bottom:1px solid #999;font-size:14px;color:var(--text);padding-bottom:8px}
.captcha{left:382px;top:462px;width:211px;height:49px;border:1px solid #ccc;display:flex;align-items:center;gap:10px;padding-left:10px;font-size:13px;background:#fafafa}
.captcha i{width:22px;height:22px;border:2px solid #bbb;background:var(--white);display:block}
.captcha em{margin-left:auto;margin-right:12px;width:18px;height:18px;border-radius:50%;background:#9bb4d8;display:block}
.contact-card .btn{left:688px;top:462px;width:183px;height:49px;background:var(--dark);font-size:18px}

.footer-mark{left:560px;top:197px;width:80px;height:80px;border-radius:50%;background:var(--green)}
.footer-links{top:307px;display:flex;justify-content:center;gap:36px}
.footer-links a{color:var(--white);font-size:17px;text-decoration:none;font-family:"Open Sans",sans-serif}
.copy{top:361px;color:var(--white);font-size:16px}
</style>
</head>
<body>

<div class="abs topbar"><span>Free Design Consultation</span></div>

<header class="abs header">
  <div class="abs brand"><div class="brand-mark"></div><div class="brand-name">Maple Yard Works</div></div>
  <div class="abs info" style="left:444px">
    <svg viewBox="0 0 42 42" fill="none" stroke="#9bcb3b" stroke-width="2"><path d="M4 22 L21 8 L38 22"/><path d="M9 18 V36 H33 V18"/><rect x="17" y="25" width="8" height="11"/></svg>
    <div><b>Homeowners</b><small>Get Information</small></div>
  </div>
  <div class="abs info" style="left:684px">
    <svg viewBox="0 0 42 42" fill="#9bcb3b"><path d="M18 4h6l1 5 4 2 4-3 4 4-3 4 2 4 5 1v6l-5 1-2 4 3 4-4 4-4-3-4 2-1 5h-6l-1-5-4-2-4 3-4-4 3-4-2-4-5-1v-6l5-1 2-4-3-4 4-4 4 3 4-2z"/><circle cx="21" cy="21" r="6" fill="#fff"/></svg>
    <div><b>Installers</b><small>Resources &amp; Benefits</small></div>
  </div>
  <div class="abs info" style="left:918px">
    <svg viewBox="0 0 42 42" fill="#9bcb3b" style="width:32px;height:32px"><path d="M9 3l7 1 3 9-4 3c2 5 6 9 11 11l3-4 9 3 1 7c-2 3-5 5-9 4C19 35 7 23 5 12c-1-4 1-7 4-9z"/></svg>
    <div><b>888.888.8888</b><small>info@mapleyardworks.com</small></div>
  </div>
</header>

<nav class="abs nav">
  <a>Home</a><a>Services</a><a>Gallery</a><a>Store</a><a>About Us</a><a>Info</a><a>Contact Us</a>
</nav>

<section class="abs hero" role="img" aria-label="Brick family house with a wide green front lawn">
  <h1 class="abs hero-title">Maple Yard Works</h1>
  <p class="abs hero-text">Lorem ipsum dolor sit amet, consectetur adipiscing elit.<br>Morbi nec lorem ut diam facilisis rutrum sed et diam.</p>
  <a class="btn">Get A Free Quote Now <svg viewBox="0 0 10 14"><path d="M2 1l6 6-6 6" stroke="#222" stroke-width="2.4" fill="none"/></svg></a>
  <div class="abs dots"><i></i><i class="on"></i><i></i></div>
</section>

<section class="abs about">
  <h2 class="abs heading">About Us</h2>
  <p class="abs">Lorem ipsum dolor sit amet, consectetur adipiscing elit. Morbi nec lorem ut diam facilisis rutrum sed et diam. Curabitur semper efficitur varius. Ut egestas convallis quam. Integer vehicula, mauris vel facilisis eleifend, lorem leo porta eros, id congue nibh eros eleifend velit. Integer cursus non libero at pretium.</p>
  <a class="btn">Read More <svg viewBox="0 0 10 14"><path d="M2 1l6 6-6 6" stroke="#fff" stroke-width="2.4" fill="none"/></svg></a>
  <div class="abs about-photo" role="img" aria-label="Installer laying rolls of turf beside a paver patio"></div>
</section>

<section class="abs services">
  <h2 class="abs heading center">Our Services</h2>
  <p class="abs lead center">Lorem ipsum dolor sit amet, consectetur adipiscing elit. Morbi nec lorem ut diam facilisis rutrum sed et diam.<br>Curabitur semper efficitur varius. Ut egestas convallis quam. Integer vehicula,</p>
  <div class="abs service" style="left:89px;top:216px">
    <div class="ring" role="img" aria-label="Synthetic turf lawn beside a house" style="background:linear-gradient(180deg,#9aa6a8 0%,#c7c9c4 30%,#4e8a2a 45%,#2f6d1c 100%)"></div>
    <h3>Synthetic Turf</h3>
    <p>Lorem ipsum dolor sit amet, consectetur adipiscing elit. Morbi nec lorem ut diam facilisis rutrum sed et diam...[+]</p>
  </div>
  <div class="abs service" style="left:460px;top:216px">
    <div class="ring" role="img" aria-label="Gray interlocking paver stones" style="background:linear-gradient(135deg,#8e8e8e,#a9a9a9 50%,#7c7c7c)"></div>
    <h3>Interlocking Pavers</h3>
    <p>Lorem ipsum dolor sit amet, consectetur adipiscing elit. Morbi nec lorem ut diam facilisis rutrum sed et diam...[+]</p>
  </div>
  <div class="abs service" style="left:835px;top:216px">
    <div class="ring" role="img" aria-label="Wooden patio cover over a stone fireplace lounge" style="background:linear-gradient(180deg,#c9773a 0%,#a86a3a 35%,#8c8579 65%,#6f6a5e 100%)"></div>
    <h3>Patio Covers</h3>
    <p>Lorem ipsum dolor sit amet, consectetur adipiscing elit. Morbi nec lorem ut diam facilisis rutrum sed et diam...[+]</p>
  </div>
</section>

<section class="abs gallery">
  <h2 class="abs heading center">Our Gallery</h2>
  <p class="abs lead center">Lorem ipsum dolor sit amet, consectetur adipiscing elit. Morbi nec lorem ut diam facilisis rutrum sed et diam.<br>Curabitur semper efficitur varius. Ut egestas convallis quam. Integer vehicula,</p>
  <div class="tile" role="img" aria-label="Synthetic sports turf with field lines" style="left:88px;top:248px;width:246px;height:253px;background:linear-gradient(135deg,#4b8d2a,#6aae36)"></div>
  <div class="tile" role="img" aria-label="Roll of artificial grass" style="left:347px;top:248px;width:246px;height:253px;background:linear-gradient(135deg,#5fa72c,#3f8a1f)"></div>
  <div class="tile" role="img" aria-label="Covered concrete patio with fire pit and landscaped yard" style="left:609px;top:248px;width:503px;height:253px;background:linear-gradient(135deg,#3e4652 0%,#7a7f82 40%,#9b9890 70%,#657a48 100%)"></div>
  <div class="tile" role="img" aria-label="Modern house with paver walkway and shrubs" style="left:88px;top:517px;width:508px;height:252px;background:linear-gradient(180deg,#5b6a5a 0%,#4a5360 40%,#b3b0a6 75%,#6b8a3a 100%)"></div>
  <div class="tile" role="img" aria-label="Red brick herringbone pavers" style="left:609px;top:517px;width:246px;height:252px;background:linear-gradient(135deg,#c47a52,#b2653e 50%,#cf8e63)"></div>
  <div class="tile" role="img" aria-label="Decorative red and white interlocking pavers" style="left:864px;top:517px;width:248px;height:252px;background:linear-gradient(135deg,#8d8d8f,#b04a3c 40%,#d6d6d6 65%,#6f7073)"></div>
  <a class="btn">View Gallery More <svg viewBox="0 0 10 14"><path d="M2 1l6 6-6 6" stroke="#fff" stroke-width="2.4" fill="none"/></svg></a>
</section>

<section class="abs testimonials">
  <div class="abs quote-box"><svg width="40" height="32" viewBox="0 0 40 32" fill="#9bcb3b"><path d="M2 16C2 7 7 2 15 1v6c-4 1-6 4-6 8h6v16H2zM23 16c0-9 5-14 13-15v6c-4 1-6 4-6 8h6v16H23z"/></svg></div>
  <h2 class="abs heading center">What &nbsp;Our Client Say!</h2>
  <div class="abs card" style="left:134px">
    <div class="avatar" role="img" aria-label="Customer portrait"></div>
    <div class="who"><b>Marcus</b><small>Customer</small></div>
    <svg class="qmark" width="40" height="30" viewBox="0 0 40 32" fill="#d8ebb1"><path d="M38 16c0 9-5 14-13 15v-6c4-1 6-4 6-8h-6V1h13zM17 16c0 9-5 14-13 15v-6c4-1 6-4 6-8H4V1h13z"/></svg>
    <p>Lorem ipsum dolor sit amet, consectetur adipiscing elit. Morbi nec lorem ut diam facilisis rutrum sed et diam. Curabitur semper efficitur varius. Ut egestas convallis quam. Integer vehicula... <a>Read More</a></p>
  </div>
  <div class="abs card" style="left:633px">
    <div class="avatar" role="img" aria-label="Customer portrait"></div>
    <div class="who"><b>Elena</b><small>Customer</small></div>
    <svg class="qmark" width="40" height="30" viewBox="0 0 40 32" fill="#d8ebb1"><path d="M38 16c0 9-5 14-13 15v-6c4-1 6-4 6-8h-6V1h13zM17 16c0 9-5 14-13 15v-6c4-1 6-4 6-8H4V1h13z"/></svg>
    <p>Lorem ipsum dolor sit amet, consectetur adipiscing elit. Morbi nec lorem ut diam facilisis rutrum sed et diam. Curabitur semper efficitur varius. Ut egestas convallis quam. Integer vehicula... <a>Read More</a></p>
  </div>
  <a class="btn">View All Testimonials <svg viewBox="0 0 10 14"><path d="M2 1l6 6-6 6" stroke="#fff" stroke-width="2.4" fill="none"/></svg></a>
</section>

<section class="abs contact"></section>
<footer class="abs footer">
  <div class="abs footer-mark"></div>
  <div class="abs footer-links center"><a>Home</a><a>Synthetic</a><a>Gallery</a><a>Store</a><a>About Us</a><a>Info</a><a>Contact Us</a></div>
  <p class="abs copy center">Copyright © 2019 Maple Yard Works.All Rights Reserved</p>
</footer>

<div class="abs contact-card">
  <h2 class="abs heading">Contact Us</h2>
  <div class="abs touch">
    <h4>Get In Touch</h4>
    <div class="row" style="top:112px;border-top:0"><svg viewBox="0 0 16 18" fill="#fff"><path d="M8 0a6 6 0 0 1 6 6c0 5-6 12-6 12S2 11 2 6a6 6 0 0 1 6-6zm0 3.5a2.5 2.5 0 1 0 0 5 2.5 2.5 0 0 0 0-5z"/></svg><span>2840 Orchard Bend Suite<br>C, Fenwick, CA 90210</span></div>
    <div class="row" style="top:172px;padding-top:18px"><svg viewBox="0 0 42 42" fill="#fff"><path d="M9 3l7 1 3 9-4 3c2 5 6 9 11 11l3-4 9 3 1 7c-2 3-5 5-9 4C19 35 7 23 5 12c-1-4 1-7 4-9z"/></svg><span>888 888 8888</span></div>
    <div class="row" style="top:226px;padding-top:18px"><svg viewBox="0 0 16 18" fill="none" stroke="#fff" stroke-width="1.6"><rect x="1" y="4" width="14" height="10"/><path d="M1 4l7 6 7-6"/></svg><span>info@mapleyardworks.com</span></div>
    <div class="row" style="top:282px;height:1px"></div>
  </div>
  <div class="abs talk">LET'S TALK</div>
  <div class="abs field" style="top:228px">Your Name</div>
  <div class="abs field" style="top:278px">Email Address</div>
  <div class="abs field" style="top:328px">Phone Number</div>
  <div class="abs field" style="top:378px;padding-bottom:35px">Message</div>
  <div class="abs captcha"><i></i>I'm not a Robot<em></em></div>
  <a class="btn">Submit <svg viewBox="0 0 10 14"><path d="M2 1l6 6-6 6" stroke="#fff" stroke-width="2.4" fill="none"/></svg></a>
</div>

</body>
</html>
```